The Vixen Rides Again Line of Sparkling Wine & Spirits

Back info: Tara Rose Whitfield Owner 209-555-0143 1480 E. Harlow Rd, Bldg. 7, & 8, Lodi Ca. 95299
Sparkling Wines & Memorabilia www.thevixenridesagain.example
Ok I have uploaded the winning design. The color that I am after is the Fushia, Raspberry, Red, Matte Satin Matalic Finish. With a 24 Karet Gold color Foil. The Bottle is on the top row and it's the 2nd Bottle in. That is the Color that I want. This is the style of font. Make sure that you put what we're advertising. Good Luck to you all. Warmest regards, Tara
Target Market(s)
21 & up UniSex
Industry/Entity Type
Sparkling Wine and Memorabilia
Contact Information for Business Card
there listed up above.....

```html
<!DOCTYPE html>
<html lang="en">
<head>
<meta charset="utf-8">
<title>The Vixen Rides Again — Business Card</title>
<link href="https://fonts.googleapis.com/css2?family=Poppins:wght@400;600&family=Pinyon+Script&display=swap" rel="stylesheet">
<style>
  :root {
    --backdrop: #cfcfcf;
    --backdrop-edge: #b4b4b4;
    --card-black: #151515;
    --card-white: #ffffff;
    --foil-gold: #e2b33a;
    --ink: #1a1a1a;
    --ink-soft: #2b2b2b;
    --silver: #e6e6e6;
  }
  * { margin: 0; padding: 0; box-sizing: border-box; }
  html, body { width: 1200px; height: 1015px; overflow: hidden; }
  body {
    background: radial-gradient(ellipse at 50% 40%, var(--backdrop) 0%, var(--backdrop-edge) 100%);
    font-family: "Poppins", sans-serif;
    position: relative;
  }
  .card {
    position: absolute;
    width: 620px;
    height: 354px;
    box-shadow: 0 10px 24px rgba(0,0,0,0.35);
  }
  /* Front */
  .card-front {
    left: 70px; top: 70px;
    background: var(--card-black);
  }
  .front-brand {
    position: absolute;
    left: 0; right: 0; top: 118px;
    text-align: center;
    font-weight: 600;
    font-size: 40px;
    color: var(--foil-gold);
    letter-spacing: 0.5px;
  }
  .front-tagline {
    position: absolute;
    left: 170px; top: 210px;
    display: flex; align-items: center; gap: 10px;
    color: var(--silver);
    font-size: 15px;
    letter-spacing: 1.5px;
    text-transform: uppercase;
  }
  .sparkle-mark { width: 26px; height: 34px; }
  /* Back */
  .card-back {
    left: 510px; top: 590px;
    background: var(--card-white);
  }
  .back-brand {
    position: absolute;
    right: 60px; top: 48px;
    font-weight: 600;
    font-size: 30px;
    color: var(--ink);
  }
  .divider {
    position: absolute;
    height: 1px;
    background: var(--ink);
  }
  .divider-top { left: 300px; right: 30px; top: 112px; }
  .divider-bottom { left: 36px; right: 260px; top: 264px; }
  .address {
    position: absolute;
    right: 30px; top: 128px;
    text-align: right;
    font-size: 15px;
    line-height: 1.35;
    color: var(--ink-soft);
  }
  .holder {
    position: absolute;
    left: 36px; top: 200px;
  }
  .holder-name {
    font-family: "Pinyon Script", cursive;
    font-size: 32px;
    line-height: 1;
    color: var(--ink);
  }
  .holder-role {
    font-size: 15px;
    color: var(--ink-soft);
  }
  .contacts {
    position: absolute;
    left: 36px; top: 276px;
    list-style: none;
    font-size: 15px;
    line-height: 1.4;
    color: var(--ink-soft);
  }
  .contacts li { display: flex; align-items: center; gap: 10px; }
  .contacts svg { width: 14px; height: 14px; flex: none; }
</style>
</head>
<body>
  <section class="card card-front">
    <div class="front-brand">The Vixen Rides Again</div>
    <div class="front-tagline">
      <svg class="sparkle-mark" role="img" aria-label="Small sparkle stars" viewBox="0 0 26 34">
        <circle cx="13" cy="17" r="9" fill="#ffffff" opacity="0.25"/>
      </svg>
      <span>Sparkling Wines &amp; Memorabilia</span>
    </div>
  </section>

  <section class="card card-back">
    <div class="back-brand">The Vixen Rides Again</div>
    <div class="divider divider-top"></div>
    <address class="address" style="font-style:normal">
      1480 E. Harlow Rd<br>
      Bldg. 7, &amp; 8<br>
      Lodi Ca. 95299
    </address>
    <div class="holder">
      <div class="holder-name">Tara Rose Whitfield</div>
      <div class="holder-role">Owner</div>
    </div>
    <div class="divider divider-bottom"></div>
    <ul class="contacts">
      <li>
        <svg viewBox="0 0 16 16"><path d="M4 1.5l2.2 3-1.3 1.6c.9 2 2.3 3.4 4.3 4.3l1.6-1.3 3 2.2-1.3 2.6C7.3 13.6 2.4 8.7 1.6 3.5z" fill="#1a1a1a"/></svg>
        <span>209-555-0143</span>
      </li>
      <li>
        <svg viewBox="0 0 16 16"><rect x="1" y="3" width="14" height="10" fill="#1a1a1a"/><path d="M1.5 3.5L8 9l6.5-5.5" stroke="#fff" stroke-width="1.3" fill="none"/></svg>
        <span>thequeen@thevixenridesagain.example</span>
      </li>
      <li>
        <svg viewBox="0 0 16 16"><circle cx="8" cy="8" r="6.5" fill="none" stroke="#1a1a1a" stroke-width="1.6"/><path d="M1.5 8h13M8 1.5c-3 3.5-3 9.5 0 13M8 1.5c3 3.5 3 9.5 0 13" stroke="#1a1a1a" stroke-width="1.2" fill="none"/></svg>
        <span>www.thevixenridesagain.example</span>
      </li>
    </ul>
  </section>
</body>
</html>
```